A specialised Sport management needs a corporate brochure design

We are a specialized company in the management and consultancy of sports events. and need to have a company brochure
We provide the following services;
Event management
Venues management
Production
Ticketing
Consulting
Hospitality
Activity management
Event timing
Branding of event
Event supplies
We need a corporate profile design for our company to showcase the major events that we have covered , with images, information, statistics, surveys, products and services used. We want to highlight our professionalism and execution of the events, experience of the participants, spectators . How we have grown in the past few years and reached the international standards.
Objectives of the work:
To get sponsors and partners for future business and to present Keel-Marrow
as not just a sports management company but also a professional sports
events management company.
You can check our website
www.keel-marrow.example
Target Market(s)
Sponsors and corporate partners
Industry/Entity Type
Events
Font styles to use
Requirements
Must have
- Must Have:
- - Very professional look
- -Some event images,Event information, statistics, surveys, products and services used. We want to highlight our professionalism and execution of the events (Attached)
Nice to have
- Similar momentom of the below design
- http://www.dunlathgames.example/wp-content/themes/dunlath_games/pdf/CP-2014-15-V10-Web.pdf

```html
<!DOCTYPE html>
<html lang="en">
<head>
<meta charset="utf-8">
<title>Keel-Marrow – Partnership Spread</title>
<link rel="stylesheet" href="https://fonts.googleapis.com/css2?family=Oswald:wght@500;600;700&family=Arimo:wght@400;700&display=swap">
<style>
  :root {
    --stage: #000000;
    --paper: #ffffff;
    --green: #1e6b35;
    --green-ring: #2e6a3a;
    --orange: #e8581c;
    --orange-ring: #f07a3a;
    --grey: #6d6d6d;
    --ink: #111111;
    --dot: #e8321c;
    --rock: #c9a57a;
    --rock-dark: #8a6a48;
    --sky: #2a4f9a;
  }
  * { box-sizing: border-box; margin: 0; padding: 0; }
  html, body {
    width: 1200px; height: 624px; overflow: hidden;
    background: var(--stage);
    font-family: "Arimo", Arial, sans-serif;
  }
  .spread { position: absolute; left: 27px; top: 90px; width: 1146px; height: 445px; }
  .page { position: absolute; top: 0; height: 445px; overflow: hidden; background: var(--paper); }
  .page--left { left: 0; width: 571px; }
  .page--right { left: 577px; width: 569px; }

  .photo { position: absolute; inset: 0; }
  .photo--left {
    background:
      linear-gradient(180deg, rgba(42,79,154,0.9) 0%, rgba(42,79,154,0.35) 22%, rgba(0,0,0,0) 34%),
      linear-gradient(160deg, var(--rock) 20%, #d8b88d 50%, var(--rock-dark) 100%);
  }
  .photo--left::after {
    content: ""; position: absolute; left: 0; right: 0; bottom: 0; height: 120px;
    background: linear-gradient(180deg, rgba(255,255,255,0) 0%, rgba(255,255,255,0.55) 70%, rgba(255,255,255,0.9) 100%);
    clip-path: polygon(0 40%, 20% 70%, 40% 100%, 0 100%);
  }
  .photo--right {
    width: 300px;
    background:
      linear-gradient(90deg, rgba(255,255,255,0) 55%, var(--paper) 100%),
      linear-gradient(180deg, var(--sky) 0%, #4a6fb0 30%, var(--rock) 40%, #b48f64 75%, #e9dccb 100%);
  }

  .headline {
    position: absolute; left: 45px; top: 26px;
    font-family: "Oswald", "Arial Narrow", sans-serif; font-weight: 600;
    font-size: 25px; line-height: 25px; color: var(--paper); text-transform: uppercase;
  }

  .reason {
    position: absolute; width: 104px; height: 104px; border-radius: 50%;
    background: var(--paper); display: flex; align-items: center; justify-content: center;
    text-align: center; font-weight: 700; font-size: 10.5px; line-height: 12.5px; padding: 0 10px;
  }
  .reason--orange { color: var(--orange); border: 3px solid var(--orange); box-shadow: 0 0 0 10px rgba(240,122,58,0.35); }
  .reason--green { color: var(--green); border: 3px solid var(--green-ring); box-shadow: 0 0 0 10px rgba(46,106,58,0.3); }

  .benefits { position: absolute; right: 27px; top: 22px; text-align: right; }
  .benefits__title {
    font-family: "Oswald", "Arial Narrow", sans-serif; font-weight: 700;
    font-size: 42px; line-height: 46px; color: var(--green); text-transform: uppercase;
  }
  .benefits__subtitle {
    font-family: "Oswald", "Arial Narrow", sans-serif; font-weight: 600;
    font-size: 23px; line-height: 28px; color: var(--grey); text-transform: uppercase; margin-top: 2px;
  }
  .benefit-list { list-style: none; margin-top: 6px; }
  .benefit-list li {
    display: flex; justify-content: flex-end; align-items: flex-start; gap: 8px;
    font-size: 12px; line-height: 14px; color: var(--orange); margin-bottom: 7.5px;
  }
  .benefit-list svg { flex: none; margin-top: 0; }

  .terms { position: absolute; right: 27px; bottom: 26px; text-align: right; font-size: 8.5px; line-height: 13px; color: var(--ink); }
  .terms__title { font-weight: 700; }
  .terms__item::after {
    content: ""; display: inline-block; width: 4px; height: 4px; border-radius: 50%;
    background: var(--dot); margin-left: 4px; vertical-align: middle;
  }
</style>
</head>
<body>
  <div class="spread">
    <section class="page page--left">
      <div class="photo photo--left" role="img" aria-label="Trail runners climbing down a sandy rock cliff under a blue sky"></div>
      <h1 class="headline">Why Partner<br>With Us?</h1>
      <div class="reason reason--orange" style="left:42px;top:123px;">Be part of the fastest growing Events in terms of Participation and Exposure</div>
      <div class="reason reason--orange" style="left:218px;top:123px;">Be part of the most exciting Sport Events in Kuwait</div>
      <div class="reason reason--green" style="left:42px;top:288px;">High Interaction with Participants and Spectators</div>
      <div class="reason reason--green" style="left:218px;top:288px;">Year long Exposure through our Events and Activities</div>
    </section>

    <section class="page page--right">
      <div class="photo photo--right" role="img" aria-label="Rocky desert ridge with a marshal under a blue sky, fading into white brush strokes"></div>
      <div class="benefits">
        <h2 class="benefits__title">Benefits</h2>
        <h3 class="benefits__subtitle">Partner’s Benefits</h3>
        <ul class="benefit-list">
          <li><span>Featured in all Keel-Marrow Marketing</span><svg width="14" height="14" viewBox="0 0 14 14"><circle cx="7" cy="7" r="6" fill="none" stroke="#e8581c" stroke-width="1.2"/><path d="M10 7H4M6.5 4.5 4 7l2.5 2.5" fill="none" stroke="#e8581c" stroke-width="1.2"/></svg></li>
          <li><span>Logo placement on our Website</span><svg width="14" height="14" viewBox="0 0 14 14"><circle cx="7" cy="7" r="6" fill="none" stroke="#e8581c" stroke-width="1.2"/><path d="M10 7H4M6.5 4.5 4 7l2.5 2.5" fill="none" stroke="#e8581c" stroke-width="1.2"/></svg></li>
          <li><span>Branding on event location as Event Partner</span><svg width="14" height="14" viewBox="0 0 14 14"><circle cx="7" cy="7" r="6" fill="none" stroke="#e8581c" stroke-width="1.2"/><path d="M10 7H4M6.5 4.5 4 7l2.5 2.5" fill="none" stroke="#e8581c" stroke-width="1.2"/></svg></li>
          <li><span>Free booth on location at our events<br>(minimum 3 of our events)</span><svg width="14" height="14" viewBox="0 0 14 14"><circle cx="7" cy="7" r="6" fill="none" stroke="#e8581c" stroke-width="1.2"/><path d="M10 7H4M6.5 4.5 4 7l2.5 2.5" fill="none" stroke="#e8581c" stroke-width="1.2"/></svg></li>
          <li><span>Email advertisement</span><svg width="14" height="14" viewBox="0 0 14 14"><circle cx="7" cy="7" r="6" fill="none" stroke="#e8581c" stroke-width="1.2"/><path d="M10 7H4M6.5 4.5 4 7l2.5 2.5" fill="none" stroke="#e8581c" stroke-width="1.2"/></svg></li>
          <li><span>Featured in our bi-annual newsletter</span><svg width="14" height="14" viewBox="0 0 14 14"><circle cx="7" cy="7" r="6" fill="none" stroke="#e8581c" stroke-width="1.2"/><path d="M10 7H4M6.5 4.5 4 7l2.5 2.5" fill="none" stroke="#e8581c" stroke-width="1.2"/></svg></li>
          <li><span>Exposure at our partnered event outlets</span><svg width="14" height="14" viewBox="0 0 14 14"><circle cx="7" cy="7" r="6" fill="none" stroke="#e8581c" stroke-width="1.2"/><path d="M10 7H4M6.5 4.5 4 7l2.5 2.5" fill="none" stroke="#e8581c" stroke-width="1.2"/></svg></li>
        </ul>
      </div>
      <div class="terms">
        <p class="terms__title">Partnership Terms</p>
        <p class="terms__item">Exclusivity</p>
        <p class="terms__item">Support in Marketing our events through: Social Media, Datebase, On Location</p>
      </div>
    </section>
  </div>
</body>
</html>
```